Washing powder bag design.

Project Description – Graphic Design Proposal for ORNE Laundry Powder Packaging
We have already explored initial design ideas internally, supported by AI-assisted tools (ChatGPT) to develop early concepts, layouts, and mockups. To support this, we have attached the bag die-cut, where graphics and text are placed as a visual guideline for the intended structure. In addition, we have included a mockup of the product series currently under development to clearly communicate the desired style, direction, and overall visual identity.
The mockup should be regarded as the design foundation for this project and as a starting point for professional refinement.
Scope of Work
We would like you to create three graphic design variants, each based on a different color direction:
1. Variant 1: In line with our current color scheme
2. Variant 2: A blue version
3. Variant 3: A green version
Design Elements to Be Preserved
The following elements must be maintained across all three variants:
• The overall style and visual expression of the mockup
• The leaf-shaped element in the bottom right corner
• The ORNE layout, including typography, positioning, and general look & feel
Summary
While the color palette may vary, the structure, style, and key design elements must remain consistent and be directly based on the attached mockup.
We look forward to seeing your creative interpretation and professional input.
Updates
We need the design to be created based on the attached die-cut file “Orne 10 kg BAG 202526”, including all text elements.
We would like the final to include both the designed die-cut file and a mockup.

```html
<!DOCTYPE html>
<html lang="da">
<head>
<meta charset="utf-8">
<title>ORNE Vaskepulver – 10 kg</title>
<link rel="stylesheet" href="https://fonts.googleapis.com/css2?family=Archivo:wght@600;700;800;900&display=swap">
<style>
  :root {
    --stage: #f1f1f3;
    --bag: #f4f4f6;
    --bag-shade: #e4e4e8;
    --sky: #0aa2dc;
    --navy: #0b0f8a;
    --royal: #1f4fd6;
    --deep: #101a9a;
    --line: #2a2a35;
  }
  * { margin: 0; padding: 0; box-sizing: border-box; }
  html, body { width: 966px; height: 1200px; overflow: hidden; }
  body {
    background: var(--stage);
    font-family: "Archivo", "Helvetica Neue", Arial, sans-serif;
    position: relative;
  }
  .bag {
    position: absolute;
    left: 258px; top: 152px;
    width: 450px; height: 900px;
    background: linear-gradient(90deg, var(--bag-shade) 0%, var(--bag) 8%, #ffffff 50%, var(--bag) 92%, var(--bag-shade) 100%);
    overflow: hidden;
  }
  .seal {
    position: absolute; left: 0; right: 0; top: 0; height: 18px;
    border-bottom: 1px solid #dcdce0;
  }
  .fold {
    position: absolute; left: 0; right: 0; top: 180px; height: 1px;
    background: #dcdce0;
  }
  .vent-holes {
    position: absolute; top: 50px; left: 143px;
    display: flex; gap: 10px;
  }
  .vent-holes span {
    width: 46px; height: 46px; border-radius: 50%;
    border: 1px solid var(--line);
  }
  .pattern-field { position: absolute; left: 0; top: 0; }
  .brand {
    position: absolute; left: 0; right: 0; top: 208px;
    text-align: center;
    color: var(--sky);
    font-weight: 800;
    font-size: 112px;
    letter-spacing: -3px;
    line-height: 1;
  }
  .product-name {
    position: absolute; left: 0; right: 0; top: 400px;
    text-align: center; color: var(--navy);
    font-weight: 900; font-size: 46px; letter-spacing: -1.5px; line-height: 1;
  }
  .product-sub {
    position: absolute; left: 0; right: 0; top: 455px;
    text-align: center; color: var(--navy);
    font-weight: 700; font-size: 27px; letter-spacing: -0.6px; line-height: 1;
  }
  .tagline {
    position: absolute; left: 78px; width: 290px; top: 505px;
    text-align: center; color: var(--sky);
    font-weight: 700; font-size: 19px; letter-spacing: -0.4px; line-height: 26px;
  }
  .usage {
    position: absolute; left: 366px; top: 508px; width: 72px;
    display: flex; flex-direction: column; align-items: center;
    color: var(--navy); font-weight: 800; font-size: 15px; letter-spacing: -0.3px;
  }
  .usage svg { display: block; }
  .usage .loads { margin-bottom: 2px; }
  .usage .spec { line-height: 22px; }
</style>
</head>
<body>
  <main class="bag">
    <div class="seal"></div>
    <div class="vent-holes"><span></span><span></span><span></span></div>
    <div class="fold"></div>

    <svg class="pattern-field" width="450" height="900" viewBox="0 0 450 900" role="img" aria-label="Abstract geometric artwork of overlapping blue circles, leaf shapes and halftone dots">
      <defs>
        <linearGradient id="patternTone" x1="0" y1="0" x2="1" y2="1">
          <stop offset="0" stop-color="#2fb0e6"/>
          <stop offset="0.35" stop-color="#1e6fd8"/>
          <stop offset="0.7" stop-color="#1f3fcf"/>
          <stop offset="1" stop-color="#101a9a"/>
        </linearGradient>
        <linearGradient id="patternMist" x1="0" y1="0" x2="0" y2="1">
          <stop offset="0" stop-color="#9fd8f2" stop-opacity="0"/>
          <stop offset="1" stop-color="#9fd8f2" stop-opacity="0.55"/>
        </linearGradient>
      </defs>
      <path d="M0 500 Q60 520 100 590 L0 600 Z" fill="url(#patternMist)"/>
      <path d="M0 605 Q20 586 55 588 L99 588 L99 610 L327 610 L327 720 Q371 740 371 800 Q371 858 320 900 L0 900 Z" fill="url(#patternTone)"/>
    </svg>

    <div class="brand">ORNE</div>
    <h1 class="product-name">VASKEPULVER</h1>
    <p class="product-sub">LAUNDRY DETERGENT</p>
    <p class="tagline">LIV OG BALANCE<br>I HVERDAGEN</p>

    <div class="usage">
      <span class="loads">120</span>
      <svg width="46" height="34" viewBox="0 0 46 34" fill="none" stroke="#0b0f8a" stroke-width="2.2" aria-label="Antal vaske">
        <rect x="3" y="2" width="40" height="9" rx="4.5"/>
        <rect x="3" y="12" width="40" height="9" rx="4.5"/>
        <rect x="3" y="22" width="40" height="9" rx="4.5"/>
      </svg>
      <svg width="42" height="52" viewBox="0 0 42 52" fill="none" stroke="#0b0f8a" stroke-width="2.2" style="margin-top:12px" aria-label="Vaskemaskine">
        <rect x="2" y="2" width="38" height="48" rx="2"/>
        <line x1="2" y1="12" x2="40" y2="12"/>
        <circle cx="10" cy="7" r="2"/>
        <rect x="26" y="5" width="9" height="4"/>
        <circle cx="21" cy="30" r="12"/>
        <circle cx="21" cy="30" r="7"/>
      </svg>
      <svg width="48" height="48" viewBox="0 0 48 48" fill="none" stroke="#0b0f8a" stroke-width="2.2" style="margin-top:12px" aria-label="Håndvask">
        <path d="M16 22 L30 8 M20 22 L34 10 M24 22 L36 13 M17 14 L25 6 M30 8 L40 4"/>
        <path d="M3 28 Q24 34 45 28 L41 44 L7 44 Z"/>
      </svg>
      <span class="spec" style="margin-top:10px">20-90°C</span>
      <span class="spec">10KG</span>
    </div>
  </main>
</body>
</html>
```